Roofing web site brel roofing

Look at some of our competitors web page we like something similar with NYC roofing
https://www.dovantileworks.example/
Maybe a skyline picture of nyc at the home page with a picture of flat roofing installation

Target Market(s)

Commercial and residential flat roofs

Industry/Entity Type

Flat Roofing industry

Coding

Coded - Design and coding required

Number of Pages Required

2 page

Font styles to use
Decorative
Script

Colors

Designer to choose colors to be used in the design.

Requirements
Must have
• At BREL Roofing, we are a trusted and reputable roofing company specializing in new construction flat roof installation and repair. With years of experience in the industry, we take pride in providing exceptional roofing solutions to our valued clients. Our team of highly skilled and dedicated roofing professionals understands the unique challenges and requirements of new construction projects. We work closely with builders, contractors, and architects to design and install flat roofs that meet the specific needs of each project. From commercial buildings to residential complexes, we have the expertise to deliver reliable and durable roofing solutions. When it comes to flat roof repairs, we are your go-to experts. Our experienced technicians conduct thorough inspections to identify the root cause of any issues your roof may be experiencing. We utilize the latest industry techniques and high-quality materials to efficiently repair your flat roof, ensuring its integrity and longevity. At BREL Roofing, we prioritize customer satisfaction above all else. We believe in building strong relationships with our clients by providing exceptional craftsmanship and outstanding customer service. Our team is dedicated to delivering projects on time, within budget, and to the highest standards of quality. We understand that a well-maintained roof is essential for protecting your property and ensuring the safety of its occupants. That's why we use only the best materials and employ skilled professionals who are trained in the latest roofing practices. Our commitment to excellence is evident in every project we undertake. As a fully licensed and insured roofing company, we prioritize safety and adhere to industry regulations and best practices. We take every precaution to create a safe working environment for our team and minimize any disruptions to your daily routine. When you choose BREL Roofing, you can trust that you are working with a reliable and reputable company that will deliver exceptional results. We are committed to exceeding your expectations and providing you with a roof that is built to last. Contact us today for all your new construction flat roof installation and repair needs.
Nice to have
• NYC skyline background with commercial roofing pictures of torching roofing

```html
<!DOCTYPE html>
<html lang="en">
<head>
<meta charset="utf-8">
<title>BREL Roofing</title>
<link href="https://fonts.googleapis.com/css2?family=Roboto+Condensed:wght@400;700&family=Montserrat:wght@400;500;600;700&family=Allura&display=swap" rel="stylesheet">
<style>
:root{
  --orange:#f0602a;
  --ink:#111111;
  --footer:#222222;
  --text:#333333;
  --muted:#666666;
  --white:#ffffff;
  --head:'Roboto Condensed',sans-serif;
  --body:'Montserrat',sans-serif;
  --script:'Allura',cursive;
}
*{margin:0;padding:0;box-sizing:border-box}
html,body{width:1200px;height:4216px;overflow:hidden}
body{position:relative;background:var(--white);font-family:var(--body);color:var(--text)}
.abs{position:absolute}
.h{font-family:var(--head);font-weight:700;text-transform:uppercase;color:var(--ink)}
.or{color:var(--orange)}
.center{left:0;width:1200px;text-align:center}

.site-header{top:0;left:0;width:1200px;height:105px;background:var(--white)}
.social{display:flex;gap:10px}
.social span{width:40px;height:40px;border-radius:50%;background:var(--ink);display:block}
.social span:first-child{background:var(--orange)}
.brand{top:38px;left:0;width:1200px;text-align:center;font-family:var(--head);font-weight:700;font-size:30px;line-height:32px;color:var(--ink)}
.phone-tag{top:34px;left:864px;height:42px;display:flex;align-items:center}
.phone-tag .ic{width:40px;height:40px;border-radius:50%;background:var(--ink);display:flex;align-items:center;justify-content:center;position:relative;z-index:2}
.phone-tag .num{margin-left:-10px;height:36px;padding:0 38px 0 26px;background:var(--orange);clip-path:polygon(0 0,100% 0,92% 100%,0 100%);color:var(--white);font-weight:700;font-size:20px;display:flex;align-items:center}
.main-nav{top:105px;left:0;width:1200px;height:54px;background:var(--ink)}
.main-nav a{color:var(--white);font-weight:700;font-size:16px;text-decoration:none;position:absolute;top:16px}
.main-nav .active::after{content:"";position:absolute;left:-22px;right:-22px;bottom:-19px;height:3px;background:var(--orange)}

.hero{top:159px;left:0;width:1200px;height:592px}
.hero-script{top:118px;left:103px;font-family:var(--script);font-size:40px;color:var(--orange)}
.hero-title{top:168px;left:103px;font-size:48px;line-height:48px}
.btn{background:var(--orange);color:var(--white);font-family:var(--head);font-weight:700;font-size:18px;text-transform:uppercase;display:flex;align-items:center;justify-content:center}
.hero .btn{top:342px;left:105px;width:170px;height:46px}

.label{font-family:var(--head);font-size:21px;color:var(--orange);letter-spacing:1px}
.title{font-size:42px}
.about-text{top:917px;left:190px;width:820px;text-align:center;font-size:17px;line-height:27px}

.tiles{top:1130px;left:0;width:1200px;height:261px;display:flex;gap:3px}
.tile{flex:1;position:relative;color:var(--white);text-align:center}
.tile .name{position:absolute;left:0;right:0;font-family:var(--head);font-weight:700;font-size:21px;text-transform:uppercase}
.tile p{position:absolute;left:55px;right:55px;top:163px;font-size:14px;line-height:22px}

.divider{height:2px;width:112px;background:var(--orange);left:544px}
.divider::after{content:"";position:absolute;left:52px;top:-2px;width:6px;height:6px;border-radius:50%;background:var(--orange)}
.card{top:1567px;width:322px;height:417px;background:var(--white);box-shadow:0 4px 22px rgba(0,0,0,.12);text-align:center}
.card .photo{position:absolute;top:0;left:0;width:322px;height:212px}
.card .badge{position:absolute;top:145px;left:124px;width:74px;height:74px;border-radius:50%;background:var(--orange);border:3px solid var(--white);display:flex;align-items:center;justify-content:center}
.card h3{position:absolute;top:225px;left:0;width:100%;font-family:var(--head);font-weight:700;font-size:20px;line-height:22px;color:var(--ink);text-transform:uppercase}
.card p{position:absolute;top:277px;left:28px;right:28px;font-size:11px;line-height:18px;color:var(--muted)}
.card .more{position:absolute;top:348px;left:96px;width:134px;height:36px;border:2px solid var(--orange);color:var(--orange);font-family:var(--head);font-weight:700;font-size:13px;display:flex;align-items:center;justify-content:center}
.card.featured{background:var(--orange)}
.card.featured h3,.card.featured p{color:var(--white)}
.card.featured .more{color:var(--white);border-color:var(--white)}
.card.featured .badge{background:var(--white);border-color:var(--orange)}

.why{top:2084px;left:0;width:1200px;height:578px}
.why-title{top:2185px;left:654px;font-size:44px;color:var(--white)}
.why-text{top:2260px;left:655px;width:480px;font-size:14px;line-height:19.5px;color:#e6e6e6}
.why-list{top:2354px;left:655px;list-style:none}
.why-list li{display:flex;align-items:center;gap:8px;height:35px;color:var(--white);font-weight:700;font-size:15px}

.gallery{top:2845px;left:0;width:1200px;height:273px;display:flex;gap:3px}
.gallery div{flex:1}
.dots{top:3152px;left:530px;display:flex;gap:14px}
.dots span{width:38px;height:4px;background:var(--ink)}
.dots span.on{background:var(--orange)}

.contact-bg{top:3340px;left:0;width:1200px;height:330px;background:linear-gradient(180deg,#ffffff 0%,#e9ebee 100%)}
.footer-bg{top:3667px;left:0;width:1200px;height:549px;background:var(--footer)}
.contact-box{top:3366px;left:118px;width:977px;height:429px;background:var(--white)}
.field{position:absolute;border:1.5px solid #c9c9c9;font-size:14px;color:#444;padding:0 16px;display:flex;align-items:center}
.field.area{align-items:flex-start;padding-top:22px}
.send{top:320px;left:440px;width:203px;height:46px}

.f-brand{top:3870px;left:124px;font-family:var(--head);font-weight:700;font-size:27px;line-height:36px;color:var(--white)}
.f-social{top:3961px;left:128px;display:flex;gap:14px}
.f-social span{width:37px;height:37px;border-radius:50%;background:#2e2e2e;border:1px solid #555;display:block}
.f-social span:first-child{background:var(--orange);border-color:var(--orange)}
.vline{top:3808px;width:1px;height:310px;background:#3d3d3d}
.f-head{top:3874px;font-family:var(--head);font-weight:700;font-size:21px;color:var(--white);text-transform:uppercase;padding-left:12px;border-left:3px solid var(--orange);line-height:24px}
.f-links{top:3917px;left:420px;list-style:none}
.f-links li{font-size:12px;color:#ddd;height:26px}
.f-contact{top:3911px;left:636px;font-size:12px;color:#ddd;line-height:16px}
.f-contact div{display:flex;gap:10px;margin-bottom:18px}
.email{top:3916px;left:898px;width:220px;height:32px;background:var(--white);font-size:11px;color:#333;padding:10px 14px}
.subscribe{top:3958px;left:898px;width:220px;height:33px;font-size:14px}
.copyright{top:4162px;left:0;width:1200px;text-align:center;font-size:12px;color:#cfcfcf}
.copy-line{top:4133px;left:388px;width:812px;height:1px;background:#3d3d3d}
</style>
</head>
<body>

<header class="site-header abs">
  <div class="social abs" style="top:33px;left:135px"><span></span><span></span><span></span></div>
  <div class="brand abs">BREL ROOFING</div>
  <div class="phone-tag abs">
    <div class="ic"><svg width="20" height="20" viewBox="0 0 24 24"><path fill="#fff" d="M6.6 10.8c1.4 2.8 3.8 5.1 6.6 6.6l2.2-2.2c.3-.3.7-.4 1-.2 1.1.4 2.3.6 3.6.6.6 0 1 .4 1 1V20c0 .6-.4 1-1 1C10.6 21 3 13.4 3 4c0-.6.4-1 1-1h3.5c.6 0 1 .4 1 1 0 1.2.2 2.4.6 3.6.1.3 0 .7-.2 1l-2.3 2.2z"/></svg></div>
    <div class="num">(555) 014 2287</div>
  </div>
</header>

<nav class="main-nav abs">
  <a class="active" style="left:180px">HOME</a>
  <a style="left:325px">ABOUT US</a>
  <a style="left:510px">SERVICES ⌄</a>
  <a style="left:684px">PHOTO GALLERY</a>
  <a style="left:925px">CONTACT US</a>
</nav>

<section class="hero abs">
  <svg class="abs" style="top:0;left:0" width="1200" height="592" viewBox="0 0 1200 592">
    <defs>
      <linearGradient id="city" x1="0" y1="0" x2="0" y2="1"><stop offset="0" stop-color="#f3f4f5"/><stop offset="1" stop-color="#bfc5cb"/></linearGradient>
      <linearGradient id="roof" x1="0" y1="0" x2="1" y2="1"><stop offset="0" stop-color="#8fb8e0"/><stop offset=".55" stop-color="#c9ccd0"/><stop offset="1" stop-color="#3c4048"/></linearGradient>
    </defs>
    <rect width="1200" height="592" fill="url(#city)" role="img" aria-label="Faded New York City skyline"/>
    <polygon points="660,0 683,0 530,350 505,350" fill="#f0602a"/>
    <polygon points="683,0 1200,0 1200,592 510,592 530,350" fill="url(#roof)" role="img" aria-label="Roofer torching a flat roof above the city"/>
  </svg>
  <div class="hero-script abs">Brel Roofing</div>
  <h1 class="hero-title h abs">Professional<br>&amp; Affordable<br>Roofing Services</h1>
  <div class="btn abs">Contact Us &gt;</div>
</section>

<div class="label abs center" style="top:815px">WHO WE ARE</div>
<h2 class="title h abs center" style="top:848px">Brel <span class="or">Roofing</span></h2>
<p class="about-text abs">At BREL Roofing, we are a trusted and reputable roofing company specializing in new construction flat roof installation and repair. With years of experience in the industry, we take pride in providing exceptional roofing solutions to our valued clients. Our team of highly skilled and dedicated roofing professionals understands the unique challenges and requirements of new construction projects.</p>

<section class="tiles abs">
  <div class="tile" role="img" aria-label="Roofer repairing a roof leak" style="background:linear-gradient(135deg,#3a3a3a,#8a8f94 60%,#4b4f55)">
    <svg class="abs" style="top:163px;left:185px" width="50" height="46" viewBox="0 0 50 46"><path d="M5 24 25 6l20 18M11 20v22h28V20" fill="none" stroke="#fff" stroke-width="3"/></svg>
    <div class="name" style="top:217px">Roof Leak Repair</div>
  </div>
  <div class="tile" role="img" aria-label="Flashing work on a shingle roof" style="background:linear-gradient(135deg,#4a4a4a,#5e5e5e)">
    <div class="abs" style="top:40px;left:163px;width:70px;height:70px;border-radius:50%;background:var(--orange)"></div>
    <div class="name" style="top:130px">Flashing Services</div>
    <p>Lorem ipsum dolor sit amet consecte-tur adipiscing Lorem ipsum</p>
  </div>
  <div class="tile" role="img" aria-label="Waterproofing roof shingles" style="background:linear-gradient(135deg,#5a5e64,#9aa0a6 60%,#6b7076)">
    <svg class="abs" style="top:175px;left:178px" width="50" height="40" viewBox="0 0 50 40"><path d="M3 38h44M8 38l8-30h18l8 30M14 20h22M12 29h26" fill="none" stroke="#fff" stroke-width="3"/></svg>
    <div class="name" style="top:220px">Waterproofing Experts</div>
  </div>
</section>

<h2 class="title h abs center" style="top:1468px">Services <span class="or">Provide</span></h2>
<div class="divider abs" style="top:1527px"></div>

<article class="card abs" style="left:100px">
  <div class="photo" role="img" aria-label="Roofer nailing roof panels" style="background:linear-gradient(135deg,#6c7a88,#3a3f46);clip-path:polygon(0 0,100% 0,100% 100%,0 62%)"></div>
  <div class="badge"><svg width="34" height="34" viewBox="0 0 24 24"><circle cx="12" cy="8" r="4" fill="#fff"/><path d="M4 22c0-5 4-8 8-8s8 3 8 8z" fill="#fff"/></svg></div>
  <h3>Reliable Roofing<br>Professionals</h3>
  <p>As specialists in residential and commercial roofing services, we are dedicated to providing customer service</p>
  <div class="more">LEARN MORE &gt;</div>
</article>
<article class="card featured abs" style="left:447px">
  <div class="photo" role="img" aria-label="Dark roof eave over a window" style="background:linear-gradient(180deg,#8cc0e6 0%,#333 30%,#c08850 100%);clip-path:polygon(0 0,100% 0,100% 62%,0 100%)"></div>
  <div class="badge"><svg width="34" height="34" viewBox="0 0 24 24"><path d="M3 20h18M5 20V10l7-5 7 5v10M8 12h8M8 16h8" fill="none" stroke="#f0602a" stroke-width="2"/></svg></div>
  <h3>Individualized<br>Roofing Options</h3>
  <p>As specialists in residential and commercial roofing services, we are dedicated to providing customer service that is second to none.</p>
  <div class="more">LEARN MORE &gt;</div>
</article>
<article class="card abs" style="left:792px">
  <div class="photo" role="img" aria-label="White gutter and downspout" style="background:linear-gradient(135deg,#5f8c3a,#dfe2e4 60%,#a8adb2);clip-path:polygon(0 0,100% 0,100% 100%,0 100%)"></div>
  <div class="badge"><svg width="30" height="30" viewBox="0 0 24 24"><path d="M12 2 4 5v6c0 5 3.5 9 8 11 4.5-2 8-6 8-11V5z" fill="none" stroke="#fff" stroke-width="2"/><path d="M8 12l3 3 5-6" fill="none" stroke="#fff" stroke-width="2"/></svg></div>
  <h3>Satisfaction<br>Guaranteed</h3>
  <p>As specialists in residential and commercial roofing services, we are dedicated to providing customer service that is second to none.</p>
  <div class="more">LEARN MORE &gt;</div>
</article>

<section class="why abs">
  <svg class="abs" style="top:0;left:0" width="1200" height="578" viewBox="0 0 1200 578">
    <defs><linearGradient id="worker" x1="0" y1="0" x2="1" y2="1"><stop offset="0" stop-color="#a9a9a4"/><stop offset=".6" stop-color="#6d6f72"/><stop offset="1" stop-color="#2b2c2e"/></linearGradient></defs>
    <rect width="1200" height="578" fill="url(#worker)" role="img" aria-label="Roofer rolling out flat roof membrane"/>
    <polygon points="388,0 1200,0 1200,578 655,578" fill="#141414"/>
    <polygon points="432,98 452,98 622,495 600,495" fill="#f0602a"/>
  </svg>
</section>
<h2 class="why-title h abs">Why Choose <span class="or">Us</span></h2>
<p class="why-text abs">We work closely with builders, contractors, and architects to design and install flat roofs that meet the specific needs of each project. From commercial buildings to residential complexes, we have the expertise to deliver reliable and durable roofing solutions.</p>
<ul class="why-list abs">
  <li><svg width="20" height="16" viewBox="0 0 20 16"><path d="M2 8l6 6L18 2" fill="none" stroke="#f0602a" stroke-width="3"/></svg>Licensed, Bonded &amp; Insured</li>
  <li><svg width="20" height="16" viewBox="0 0 20 16"><path d="M2 8l6 6L18 2" fill="none" stroke="#f0602a" stroke-width="3"/></svg>Reliable &amp; Experienced Professional</li>
  <li><svg width="20" height="16" viewBox="0 0 20 16"><path d="M2 8l6 6L18 2" fill="none" stroke="#f0602a" stroke-width="3"/></svg>Lead Safe Certified</li>
  <li><svg width="20" height="16" viewBox="0 0 20 16"><path d="M2 8l6 6L18 2" fill="none" stroke="#f0602a" stroke-width="3"/></svg>24/7 Emergency Response</li>
  <li><svg width="20" height="16" viewBox="0 0 20 16"><path d="M2 8l6 6L18 2" fill="none" stroke="#f0602a" stroke-width="3"/></svg>Accredited Local Business</li>
</ul>

<div class="label abs center" style="top:2724px">OUR GALLERY</div>
<h2 class="title h abs center" style="top:2748px">Project Gallery</h2>
<div class="divider abs" style="top:2808px;left:542px"></div>
<section class="gallery abs">
  <div role="img" aria-label="Roof eave with gutter" style="background:linear-gradient(135deg,#7aa2c4,#e5e6e6 55%,#9ea3a8)"></div>
  <div role="img" aria-label="Worker pressure washing a tile roof" style="background:linear-gradient(135deg,#c5643c,#a4482a)"></div>
  <div role="img" aria-label="Roofer installing metal roofing" style="background:linear-gradient(135deg,#4a5058,#8a6a55 60%,#5c5450)"></div>
  <div role="img" aria-label="Insulated roof framing" style="background:linear-gradient(135deg,#b9b3a5,#8a6a4a 60%,#c9a07a)"></div>
</section>
<div class="dots abs"><span></span><span class="on"></span><span></span></div>

<div class="contact-bg abs"></div>
<div class="footer-bg abs"></div>
<div class="label abs center" style="top:3225px">GET IN TOUCH</div>
<h2 class="title h abs center" style="top:3250px">Contact <span class="or">Us</span></h2>
<div class="divider abs" style="top:3310px;left:542px"></div>

<section class="contact-box abs">
  <div class="abs" role="img" aria-label="Roofer torching down roll roofing" style="top:0;left:0;width:396px;height:429px;background:linear-gradient(160deg,#6e7176,#b9b6ae 55%,#8c8478)"></div>
  <div class="field" style="top:70px;left:438px;width:245px;height:51px">First Name</div>
  <div class="field" style="top:70px;left:693px;width:245px;height:51px">Last Name</div>
  <div class="field" style="top:134px;left:438px;width:245px;height:51px">Phone</div>
  <div class="field" style="top:134px;left:693px;width:245px;height:51px">Email address</div>
  <div class="field area" style="top:198px;left:438px;width:500px;height:104px">Leave Message</div>
  <div class="btn send abs">Send Message</div>
</section>

<div class="f-brand abs">Brel Roofing</div>
<div class="f-social abs"><span></span><span></span><span></span></div>
<div class="vline abs" style="left:388px"></div>
<div class="vline abs" style="left:598px"></div>
<div class="vline abs" style="left:873px"></div>

<div class="f-head abs" style="left:388px">Navigation</div>
<ul class="f-links abs"><li>Home</li><li>About Us</li><li>Services</li><li>Gallery</li><li>Contact Us</li></ul>

<div class="f-head abs" style="left:616px">Contact Us</div>
<div class="f-contact abs">
  <div><svg width="16" height="18" viewBox="0 0 24 24"><path d="M12 2a7 7 0 0 0-7 7c0 5 7 13 7 13s7-8 7-13a7 7 0 0 0-7-7zm0 9.5a2.5 2.5 0 1 1 0-5 2.5 2.5 0 0 1 0 5z" fill="#fff"/></svg><span>123 &nbsp;Address Line Street</span></div>
  <div><svg width="16" height="16" viewBox="0 0 24 24"><path fill="#fff" d="M6.6 10.8c1.4 2.8 3.8 5.1 6.6 6.6l2.2-2.2c.3-.3.7-.4 1-.2 1.1.4 2.3.6 3.6.6.6 0 1 .4 1 1V20c0 .6-.4 1-1 1C10.6 21 3 13.4 3 4c0-.6.4-1 1-1h3.5c.6 0 1 .4 1 1 0 1.2.2 2.4.6 3.6.1.3 0 .7-.2 1l-2.3 2.2z"/></svg><span>555-014-2287</span></div>
  <div><svg width="18" height="18" viewBox="0 0 24 24"><circle cx="12" cy="12" r="9" fill="none" stroke="#fff" stroke-width="2"/><path d="M12 7v5l3 2" fill="none" stroke="#fff" stroke-width="2"/></svg><span>Monday - Friday: 7am - 6pm<br>Saturday - Sunday: 9am-1pm</span></div>
</div>

<div class="f-head abs" style="left:885px;border-left:none">Newsletter Sign Up</div>
<div class="email abs">Email address*</div>
<div class="btn subscribe abs">Subscribe</div>

<div class="copy-line abs"></div>
<div class="copyright abs">Copyright © 2024 Brel Roofing - All Rights Reserved.</div>

</body>
</html>
```